Shiftwell Hub

Our product is a subscription-based website for doctors and medical practices. It allows contract-based doctors (locums) to book jobs with medical practices and to organise their own finances (invoicing, pension, etc). Also, it allows medical practices to post jobs, and book locums.

We need a website design that looks clean and professional. It should look easy-to-use and friendly, which will encourage users to sign up as they'll hopefully think using the system will also be simple and friendly.

As well as the homepage, we need a design for the logged-in view. This is very different to the website but equally important. It needs to be very functional. Much more like an application and less like a website.

PLEASE SUBMIT BOTH WEBSITE HOMEPAGE DESIGN AND APPLICATION DASHBOARD DESIGN.

The application is built and we already have a user interface (linked below) so we're not looking for a designer to decide what is on these pages - we already have that. We're ONLY asking for visual design. Please just make the content we have look good. You may move parts of the content around a small amount but the functionality is very much signed off now so it's only visual styling that we need addressed.

Please base the branding around the current logo, which can't be changed. You can get the logo as an EPS here : http://clients.brambleotter.co.uk/shiftwellhub/design/logo-green.eps

Here is a link to the current design for the website, and for the application dashboard:
http://clients.brambleotter.co.uk/shiftwellhub/design/

Also, here is a video we've had made which might help you with the brand:
http://clipvaultnet.com/83051726

Just in case it isn't clear, the video (linked in the main brief) is an essential part of the website homepage.

Reason: We need to spend some time looking over these designs and might ask for a few amendments to one or two in the next few days. Thanks.

Target Market(s)

Doctors and medical practices

Industry/Entity Type

Medical

Requirements
Must have
• It must have all the features that are in the linked designs - homepage and dashboard.

```html
<!DOCTYPE html>
<html lang="en">
<head>
<meta charset="utf-8">
<title>Shiftwell Hub</title>
<link href="https://fonts.googleapis.com/css2?family=Lato:wght@300;400&display=swap" rel="stylesheet">
<style>
:root{
  --green-deep:#1a9e6a;
  --green:#3cb25a;
  --green-lime:#9acb48;
  --line:#8fd3a4;
  --text:#333;
  --muted:#8a8a8a;
  --faint:#a5a5a5;
  --white:#fff;
  --black:#000;
}
*{box-sizing:border-box;margin:0;padding:0}
html,body{width:866px;height:1200px;overflow:hidden;background:var(--white)}
body{font-family:"Lato",sans-serif;font-weight:300;color:var(--text);position:relative;font-size:10px}
.abs{position:absolute}
.site-header{left:77px;top:0;width:711px;height:83px;background:linear-gradient(90deg,var(--green-deep),var(--green) 45%,var(--green-lime))}
.logo{left:64px;top:34px;color:var(--white);font-size:10.5px;font-weight:300}
.user-name{left:522px;top:25px;color:var(--white);font-size:9px}
.sign-out{left:463px;top:51px;color:var(--white);font-size:9px}
.dash-btn{left:511px;top:43px;width:99px;height:23px;border:2px solid #d8efc8;background:var(--white);color:#888;font-size:9px;display:flex;align-items:center;justify-content:center;border-radius:2px}
.main-nav a{position:absolute;top:98px;color:var(--muted);font-size:10.4px;text-decoration:none}
.video{left:118px;top:134px;width:249px;height:146px;border:3px solid;border-image:linear-gradient(90deg,#6cc58a,#b4dc8e) 1}
.video svg{position:absolute;left:101px;top:46px}
.hero-title{left:394px;top:146px;font-size:12px;color:#444}
.benefit{left:393px;font-size:11.5px;color:var(--faint)}
.btn{position:absolute;background:linear-gradient(180deg,#4cc06a,#24a04e);color:var(--white);font-size:9px;font-weight:300;display:flex;align-items:center;justify-content:center;border-radius:2px;box-shadow:0 0 0 2px #c9ecd2}
.rule{height:1px;background:var(--line)}
.col-title{font-size:11.5px;color:#444}
.col-sub{font-size:8.6px;color:var(--muted)}
.num{position:absolute;width:20px;height:20px;border:1.2px solid var(--green);border-radius:50%;font-size:10px;color:#555;display:flex;align-items:center;justify-content:center}
.feat-title{position:absolute;font-size:10.4px;color:#444}
.feat-desc{position:absolute;font-size:8.6px;color:var(--faint);line-height:12px;width:180px}
.more{position:absolute;font-size:8.6px;color:var(--faint);line-height:11px}
.tabs{left:220px;top:602px;width:422px;height:29px;border:2px solid #e4e4e4;border-radius:3px}
.tab{position:absolute;top:3px;display:flex;align-items:center;gap:6px;font-size:8.8px;color:#444}
.tab .num{position:static}
.try{left:0;width:866px;top:647px;text-align:center;font-size:12px;color:#444}
.label{font-size:8.8px;color:#444}
.radio{display:inline-block;width:9px;height:9px;border:1.2px solid var(--green);border-radius:50%;vertical-align:-1px;position:relative}
.radio.on::after{content:"";position:absolute;left:1.5px;top:1.5px;width:3.6px;height:3.6px;border-radius:50%;background:var(--green)}
.field{height:21px;border:1.5px solid #a9dc85;border-radius:3px}
.photo{left:564px;top:707px;width:170px;height:128px;border:1px solid #a9dc85;padding:3px}
.photo div{width:100%;height:100%;background:linear-gradient(90deg,#e6e3dc,#cfd6d4 55%,#b9c4c8)}
.press{top:868px;width:160px;height:87px;border:1px solid #a9dc85;border-radius:6px;padding:9px 12px 0 14px}
.press h3{font-weight:300;font-size:12px;color:#444;text-align:center;margin-bottom:6px}
.press p{font-size:8px;color:var(--faint);line-height:12px;hyphens:manual}
.footer{left:90px;top:990px;width:686px;height:206px;border:2px solid #d9eee0;border-radius:18px;overflow:hidden;background:var(--white)}
.footer .topline{position:absolute;left:60px;right:60px;top:0;height:3px;background:linear-gradient(90deg,#dff2e4,var(--green),#dff2e4)}
.quote{position:absolute;top:21px;text-align:center;font-size:8.8px;line-height:12px;color:#333}
.quote .who{color:var(--muted);margin-top:7px}
.fnav{position:absolute;left:71px;width:540px;top:88px;height:24px;border-top:1px solid var(--line);border-bottom:1px solid var(--line);display:flex;justify-content:center;gap:24px;align-items:center;font-size:8.8px;color:var(--muted)}
.finfo{position:absolute;left:0;right:0;top:118px;text-align:center;font-size:8.8px;color:var(--muted);line-height:17px}
.fbar{position:absolute;left:0;right:0;bottom:0;height:30px;background:var(--black);display:flex;justify-content:center;align-items:center;gap:16px;color:var(--white);font-size:8.8px;font-weight:400}
.accent{left:765px;top:1026px;width:7px;height:36px;background:linear-gradient(180deg,#9acb48,var(--green))}
</style>
</head>
<body>
<header class="abs site-header">
  <div class="abs logo">Shiftwell Hub</div>
  <div class="abs user-name">Mrs. Helena Ardwell</div>
  <div class="abs sign-out">Sign out</div>
  <div class="abs dash-btn">Go to Dashboard</div>
</header>
<nav class="main-nav">
  <a style="left:166px">Home</a><a style="left:238px">Locums</a><a style="left:315px">Employers</a><a style="left:404px">Pricing</a><a style="left:474px">About us</a><a style="left:561px">FAQ</a><a style="left:624px">Contact us</a>
</nav>

<div class="abs video" role="img" aria-label="Introductory video player">
  <svg width="42" height="42" viewBox="0 0 42 42"><defs><linearGradient id="pg" x1="0" y1="0" x2="1" y2="1"><stop offset="0" stop-color="#1a9e6a"/><stop offset="1" stop-color="#9acb48"/></linearGradient></defs><circle cx="21" cy="21" r="19" fill="none" stroke="url(#pg)" stroke-width="2.5"/><path d="M17 13 L28 21 L17 29Z" fill="#4cb85a"/></svg>
</div>
<div class="abs hero-title">A network for connectig locums with employers</div>
<div class="abs benefit" style="top:175px">Better connectivity</div>
<div class="abs benefit" style="top:199px">More choices</div>
<div class="abs benefit" style="top:223px">Less Paperwork</div>
<div class="abs benefit" style="top:247px">Less costs</div>
<div class="btn" style="left:558px;top:253px;width:128px;height:22px">Sign up for free tryout today</div>

<div class="abs rule" style="left:77px;top:304px;width:711px"></div>

<section>
  <div class="abs col-title" style="left:123px;top:320px">GP Locums</div>
  <div class="abs col-sub" style="left:113px;top:346px">The complete platform to organize your locum life</div>
  <div class="num" style="left:112px;top:373px">i</div>
  <div class="feat-title" style="left:139px;top:375px">Find jobs</div>
  <div class="feat-desc" style="left:139px;top:396px">Search, apply and get invited for a wide selection of job from practices and agencies</div>
  <div class="num" style="left:112px;top:429px">ii</div>
  <div class="feat-title" style="left:139px;top:430px">Do your locum admin easily admin</div>
  <div class="feat-desc" style="left:139px;top:449px;width:175px">Profile, diary management, invoicing, pen&shy;sion form, finances, tax returns</div>
  <div class="num" style="left:112px;top:482px">iii</div>
  <div class="feat-title" style="left:137px;top:485px">Create and grow Employer network</div>
  <div class="feat-desc" style="left:139px;top:503px">Create your online profile and connect with your own network of employers</div>
  <div class="btn" style="left:145px;top:548px;width:53px;height:22px">Sign up</div>
  <div class="more" style="left:216px;top:548px">More about Shiftwell<br>Hub for locums</div>
</section>
<section>
  <div class="abs col-title" style="left:438px;top:318px">Employers</div>
  <div class="abs col-sub" style="left:427px;top:344px">One stop solution for your locum needs</div>
  <div class="num" style="left:426px;top:371px">i</div>
  <div class="feat-title" style="left:452px;top:373px">Find locums</div>
  <div class="feat-desc" style="left:452px;top:392px;width:210px">Post your locum requirements. Search and employ the right locums via your E-booking systems</div>
  <div class="num" style="left:426px;top:427px">ii</div>
  <div class="feat-title" style="left:452px;top:428px">Do your locum admin easily admin</div>
  <div class="feat-desc" style="left:452px;top:449px;width:210px">Profile, locum rota management, pre-employment checks, locum market statistics</div>
  <div class="num" style="left:426px;top:480px">iii</div>
  <div class="feat-title" style="left:450px;top:482px">Create and grow locum network</div>
  <div class="feat-desc" style="left:451px;top:502px">Create your online profile and connect with your own network of employers</div>
  <div class="btn" style="left:452px;top:548px;width:53px;height:22px">Sign up</div>
  <div class="more" style="left:528px;top:548px">More about Shiftwell<br>Hub for locums</div>
</section>

<div class="abs rule" style="left:79px;top:582px;width:711px"></div>

<div class="abs tabs">
  <div class="tab" style="left:14px"><span class="num">i</span>The network of locums and employers</div>
  <div class="tab" style="left:209px"><span class="num">ii</span>Save time &amp; cost</div>
  <div class="tab" style="left:315px"><span class="num">iii</span>Try it free now</div>
</div>
<div class="abs try">Try it now with just an email address, GMC number and password !</div>

<form>
  <div class="abs label" style="left:159px;top:690px;color:var(--muted)">i am &nbsp;&nbsp;&nbsp;&nbsp;<span class="radio on"></span>&nbsp;&nbsp;a locum &nbsp;&nbsp;&nbsp;&nbsp;<span class="radio"></span>&nbsp;&nbsp;an employer</div>
  <div class="abs label" style="left:146px;top:711px">Email</div>
  <div class="abs field" style="left:144px;top:730px;width:161px"></div>
  <div class="abs label" style="left:372px;top:711px">GMC Number</div>
  <div class="abs field" style="left:366px;top:730px;width:160px"></div>
  <div class="abs label" style="left:147px;top:771px">Password</div>
  <div class="abs field" style="left:144px;top:786px;width:161px"></div>
  <div class="abs label" style="left:372px;top:768px">Confirm Password</div>
  <div class="abs field" style="left:366px;top:786px;width:160px"></div>
  <div class="abs label" style="left:145px;top:826px;color:var(--muted)"><span class="radio on"></span>&nbsp; i agree to the <span style="color:#333">terms of service</span> and <span style="color:#333">privacy policy</span></div>
  <div class="btn" style="left:471px;top:822px;width:54px;height:21px">Sign up</div>
</form>
<div class="abs photo"><div role="img" aria-label="Photo of a doctor talking with a smiling older patient"></div></div>

<div class="abs press" style="left:169px"><h3>Herald Daily</h3><p>Lorem Ipsum dolor sit amet, consec&shy;tetuer adipiscingelit. Duis tellus. Donec ante dolor, iaculis nec, grav&shy;idaac, cursus in, eros</p></div>
<div class="abs press" style="left:347px"><h3>Morning Post</h3><p>Lorem Ipsum dolor sit amet, consec&shy;tetuer adipiscingelit. Duis tellus. Donec ante dolor, iaculis nec, gravidaac, cursus in, eros</p></div>
<div class="abs press" style="left:521px"><h3>The Courier</h3><p>Lorem Ipsum dolor sit amet, consec&shy;tetuer adipiscingelit. Duis tellus. Donec ante dolor, iaculis nec, gravidaac, cursus in, eros</p></div>

<footer class="abs footer">
  <div class="topline"></div>
  <div class="quote" style="left:98px;width:176px">So easy to setup five minutes and you are in. And it does all the boaring admin stuff that i hate.<div class="who">Name of person, locum</div></div>
  <div class="quote" style="left:365px;width:205px">As a practice, it's great to be able to find locums quickly and easily. No more time cosuming agency phone calls !<div class="who">Blah medical centre</div></div>
  <div class="fnav"><span>Home</span><span>Locums</span><span>Employers</span><span>Pricing</span><span>About us</span><span>FAQ</span><span>Contact us</span></div>
  <div class="finfo">We are here to help : support@shiftwellhub.co.uk<br>Copyright © 2013 Shiftwell Hub Ltd. All rights reserved<br>Registered in England no. 08214597</div>
  <div class="fbar"><span>Terms of service</span><span>Privacy policy</span><span>Refund policy</span></div>
</footer>
<div class="abs accent"></div>
</body>
</html>
```